BUSINESS CARD DESIGN FOR CONSULTING BUSINESS

I need a business card design containing my logo and slogan for my new consulting business. The consulting business provides the following services: 1) human resource services assistance (payroll, expert advice, developing strategic and recruitment plans and blogs) for small businesses and 2) develops content for small business blogs and online magazines. I plan to expand the business, so I don't want to focus on the services but rather on my initials (LT) for name recognition and the name of the company, Dunmore Advisory Services.
My slogan is Relevant, Innovative, Expert Solutions.
I want a business card that is plain and not busy and contains a logo that reflects my work: consulting and writing. I would also like the business card to include the following contact information in this order: Lena Tolliver, Principal (lst line) Sr. Consultant (2nd line), 4730 Pellman Street, #502317, Sacramento, CA 95824, (3rd line) ltolliveradvisory@quillpost.net, (4th line), (916) 555-0172 (5th line), (my name, title, business address, email address, and phone number). My business's logo and name, Dunmore Advisory Services, should appear next to each other on the front of the card. The slogan should also be noted on the back of the card. Thanks!

Target Market(s)

Small businesses and governments.

Industry/Entity Type

Human Resources (HR) and Writing, but please focus on consulting services which can be both (HR and writing) or neither.

Logo Text

If possible, please create a abstract logo like the attachment. Or create a logo using my first and last initials (LT) and the word consulting like the Rupert Vane (RV) example below.

Logo styles of interest
Abstract Logo
Wordmark Logo
Lettermark Logo
Font styles to use
Serif

Colors

Designer to choose colors to be used in the design.

Requirements
Must have
• Please feel free to create your own design as the attachment is just an example to show that I prefer a simple design with that format/layout if possible. The logo should be simple like a lettermark, word mark or abstract logo with the logo on the front and the slogan on the back. Please note my contact information in this order: my name with a title of Principal/Sr. Consultant, my address, email address and my phone number..
Nice to have
• Please see the attached sample design. A blue, or green or blue violet color card may look great. I am also good with simple black and white. Thanks!
Should not have
• Large, busy logo

```html
<!DOCTYPE html>
<html lang="en">
<head>
<meta charset="utf-8">
<title>Dunmore Advisory Services – Business Card</title>
<link rel="stylesheet" href="https://fonts.googleapis.com/css2?family=Montserrat:wght@400;500&display=swap">
<style>
  :root {
    --ink: #1c1c1c;
    --paper: #ffffff;
    --text: #2a2626;
    --edge: #8a8a8a;
  }
  * { margin: 0; padding: 0; box-sizing: border-box; }
  html, body { width: 1200px; height: 1200px; overflow: hidden; background: var(--paper); }
  body { position: relative; font-family: "Montserrat", Arial, sans-serif; color: var(--text); }

  .card { position: absolute; left: 279px; width: 649px; height: 435px; }
  .card-front { top: 131px; background: var(--ink); }
  .card-back { top: 641px; background: var(--paper); border-left: 1px solid var(--edge); border-right: 1px solid var(--edge); }

  .brand { position: absolute; display: flex; align-items: center; }
  .brand-mark { flex: none; border-radius: 50%; }
  .brand-name { font-weight: 500; text-transform: uppercase; letter-spacing: 0.02em; }

  .card-front .brand { left: 163px; top: 155px; }
  .card-front .brand-mark { width: 106px; height: 106px; border: 8px solid var(--paper); margin-right: 22px; }
  .card-front .brand-name { color: var(--paper); font-size: 27px; line-height: 31px; }

  .card-back .brand { left: 185px; top: 61px; }
  .card-back .brand-mark { width: 94px; height: 94px; border: 7px solid var(--ink); margin-right: 19px; }
  .card-back .brand-name { color: var(--ink); font-size: 25px; line-height: 27px; }

  .bands { position: absolute; left: 0; top: 0; width: 649px; height: 435px; }

  .holder { position: absolute; left: 45px; top: 225px; }
  .holder-name { font-size: 21px; font-weight: 500; text-transform: uppercase; letter-spacing: 0.01em; }
  .holder-rule { width: 12px; height: 2px; background: var(--ink); margin: 8px 0 0 3px; }
  .holder-title { font-size: 18px; margin: 6px 0 0 2px; letter-spacing: 0.02em; }

  .contact { position: absolute; left: 342px; top: 263px; list-style: none; font-size: 15.5px; }
  .contact li { display: flex; align-items: flex-start; line-height: 17px; }
  .contact li + li { margin-top: 8px; }
  .contact li.phone { margin-top: 16px; }
  .contact svg { flex: none; width: 12px; height: 14px; margin: 1px 6px 0 0; fill: var(--ink); }
  .contact .address-line2 { display: block; margin-left: -5px; }
</style>
</head>
<body>

  <section class="card card-front">
    <div class="brand">
      <span class="brand-mark"></span>
      <p class="brand-name">Dunmore<br>Advisory<br>Services</p>
    </div>
  </section>

  <section class="card card-back">
    <svg class="bands" viewBox="0 0 649 435" aria-hidden="true">
      <polygon fill="var(--ink)" points="0,0 242,0 221,20 0,20"/>
      <polygon fill="var(--ink)" points="251,0 649,0 649,13 239,13"/>
      <polygon fill="var(--ink)" points="0,423 409,423 398,435 0,435"/>
      <polygon fill="var(--ink)" points="429,416 649,416 649,435 407,435"/>
    </svg>

    <div class="brand">
      <span class="brand-mark"></span>
      <p class="brand-name">Dunmore<br>Advisory<br>Services</p>
    </div>

    <div class="holder">
      <h1 class="holder-name">Lena Tolliver, Principal</h1>
      <div class="holder-rule"></div>
      <p class="holder-title">Sr. Consultant</p>
    </div>

    <ul class="contact">
      <li class="address">
        <svg viewBox="0 0 12 16"><path d="M6 0a6 6 0 0 0-6 6c0 4.5 6 10 6 10s6-5.5 6-10a6 6 0 0 0-6-6zm0 8.5A2.5 2.5 0 1 1 6 3.5a2.5 2.5 0 0 1 0 5z"/></svg>
        <span>4730 Pellman Street, #502317,<span class="address-line2">Sacramento, CA 95824</span></span>
      </li>
      <li class="email">
        <svg viewBox="0 0 12 12"><circle cx="6" cy="6" r="6"/><rect x="3" y="4" width="6" height="4.2" fill="#fff"/><path d="M3 4l3 2.3L9 4" stroke="#1c1c1c" stroke-width="0.8" fill="none"/></svg>
        <span>ltolliveradvisory@quillpost.net</span>
      </li>
      <li class="phone">
        <svg viewBox="0 0 12 12"><circle cx="6" cy="6" r="6"/><path d="M4 3.2c.4-.3.8-.2 1 .2l.4.9c.1.3 0 .6-.2.8l-.3.2c.3.7.9 1.3 1.6 1.6l.2-.3c.2-.2.5-.3.8-.2l.9.4c.4.2.5.6.2 1-.5.7-1.3.9-2.1.5A5.6 5.6 0 0 1 3.5 5.3c-.4-.8-.2-1.6.5-2.1z" fill="#fff"/></svg>
        <span>(916) 555-0172</span>
      </li>
    </ul>
  </section>

</body>
</html>
```